Recruiting agency needs corporate presentation

We are a recruiting agency specialized in life sciences. We need a corporate presentation that will be sent to our clients and prospects in a PDF format.

Details of the presentation:
- a "brochure" type of presentation, VERTICAL, with 5 pages (please see "content" file attached) The presentation will be sent in a PDF format to our prospect clients by e-mail, so the choice of images and organization need to take that into account.
- In the attachment, you will find our logo "Harlow & Associates".
- the presentation needs to convey our industry (life sciences, healthcare) and a high level of professionalism/leadership We want a sophisticated and elegant brochure.
- page 2 of the brochure needs to contain all the logos attached, in a very elegant, clear and organized way.
- page 3 shows a map with cursors (please see content file). The following countries/continents on the map need to be highlighted: USA, Brazil, Europe, North Africa, South Africa, China. We need "cursors" like pins to show where on the map our offices are: Miami, Boston, Lausanne, Denmark, Paris, Copenhaguen.
- page 4 includes pie charts (please see "Statistics 2020" Excel file): please improve the pie charts aesthetics, it needs to look very modern.

Target Market(s)

Healthcare / Life Sciences.

Requirements
Must have
• Very modern and aesthetics. I included a presentation of companies that we like to give you an indication of the overall style we're looking for.

```html
<!DOCTYPE html>
<html lang="en">
<head>
<meta charset="utf-8">
<title>Harlow & Associates — Corporate Brochure</title>
<link href="https://fonts.googleapis.com/css2?family=Montserrat:wght@400;500;600;700&family=Lato:wght@300;400;700&display=swap" rel="stylesheet">
<style>
:root{
  --bg:#dde1e6;
  --navy:#1f3f5f;
  --navy-deep:#19354f;
  --teal:#56c3c4;
  --blue:#3aa0dc;
  --lime:#b5cf3a;
  --purple:#5b4f9e;
  --sea:#3b8a7d;
  --grey:#8b97a3;
  --ink:#2c3a48;
  --paper:#ffffff;
}
*{margin:0;padding:0;box-sizing:border-box}
html,body{width:1200px;height:4807px;overflow:hidden;background:var(--bg)}
body{position:relative;font-family:'Lato',sans-serif;color:var(--ink)}
.page{position:absolute;left:296px;width:608px;height:860px;overflow:hidden;box-shadow:0 4px 14px rgba(20,40,60,.12)}
.page--cover{top:125px;background:var(--navy)}
.page--clients{top:1032px;background:var(--navy)}
.page--offices{top:1937px;background:var(--paper)}
.page--stats{top:2844px;background:var(--navy)}
.page--contact{top:3751px;background:var(--navy)}

.brand{display:flex;align-items:center;gap:8px;font-family:'Montserrat',sans-serif;font-weight:700;font-size:11px;letter-spacing:2px;color:var(--navy)}
.brand__dot{width:18px;height:18px;border-radius:50%;background:var(--navy)}
.url{font-family:'Montserrat',sans-serif;font-weight:600;font-size:12px;color:var(--teal);letter-spacing:.5px}
.folio{font-size:7px;color:var(--grey)}

/* cover */
.cover__head{position:absolute;left:0;top:0;width:100%;height:134px;background:var(--paper)}
.cover__head .brand{position:absolute;left:58px;top:58px}
.photo{position:absolute;background:linear-gradient(135deg,#c7d3de 0%,#7f93a8 45%,#4a6683 100%)}
.cover__photo{left:0;top:134px;width:100%;height:420px}
.cover__title{position:absolute;left:58px;top:468px;font-family:'Montserrat',sans-serif;font-weight:600;font-size:38px;line-height:43px;letter-spacing:4px;color:#fff}
.cover__title span{color:var(--teal)}
.cover__text{position:absolute;left:58px;top:660px;width:494px;font-size:12.5px;line-height:22px;color:#e3ebf2}
.cover__text p+p{margin-top:8px}
.cover__url{position:absolute;right:56px;top:795px}

/* clients */
.clients__sheet{position:absolute;left:52px;top:45px;width:504px;height:780px;background:var(--paper)}
.clients__sheet .brand{position:absolute;left:186px;top:28px}
.logo-grid{position:absolute;left:26px;width:452px;display:grid;grid-template-columns:repeat(6,1fr);row-gap:15px;column-gap:8px}
.logo-grid--top{top:88px}
.logo-grid--bottom{top:455px}
.logo{height:30px;display:flex;align-items:center;justify-content:center;font-family:'Lato',sans-serif;font-weight:700;font-size:10px;line-height:12px;color:var(--navy);text-align:center}
.clients__band{position:absolute;left:46px;top:400px;width:516px;height:72px;background:var(--teal);display:flex;align-items:center;padding:0 22px;color:#fff}
.band__small{font-size:12px;line-height:15px;width:110px;color:#eaf8f8}
.band__chev{font-size:28px;font-weight:300;width:36px}
.band__big{font-family:'Montserrat',sans-serif;font-weight:600;font-size:17px;line-height:20px;letter-spacing:1px;color:var(--navy);text-align:center}
.band__to{font-size:12px;margin:0 26px;color:#eaf8f8}
.clients__foot{position:absolute;left:0;bottom:14px;width:100%;padding:0 8px;display:flex;justify-content:space-between;align-items:flex-end}
.clients__foot .note{font-size:7px;color:var(--grey)}

/* offices */
.rule{position:absolute;left:58px;top:46px;width:494px;height:1px;background:#b9c2cb}
.offices__intro{position:absolute;left:58px;top:118px;width:494px;font-size:11px;line-height:16px;color:var(--ink)}
.offices__intro p+p{margin-top:10px}
.offices__intro b{color:var(--blue)}
.label{font-family:'Montserrat',sans-serif;font-size:12px;letter-spacing:.5px;color:var(--ink);position:absolute;left:58px}
.map{position:absolute;left:62px;top:320px;width:486px;height:230px;background:linear-gradient(160deg,#2a4c6e,var(--navy) 60%,#3d7f95)}
.city{position:absolute;height:26px;width:110px;background:var(--blue);color:#fff;font-family:'Montserrat',sans-serif;font-weight:600;font-size:11px;letter-spacing:1px;display:flex;align-items:center;justify-content:center}
.pin-lines{position:absolute;left:0;top:0}
.arc{position:absolute;left:0;top:0}
.bubble{position:absolute;width:54px;height:54px;border-radius:50%;background:var(--navy);color:#fff;font-size:11px;line-height:13px;display:flex;align-items:center;justify-content:center;text-align:center}
.offices__url{position:absolute;left:232px;top:820px}
.offices__folio{position:absolute;right:52px;top:825px}

/* stats */
.stats__lead{position:absolute;left:58px;top:112px;width:500px;color:#fff;font-size:20px;line-height:27px;font-weight:300}
.stats__lead p+p{margin-top:10px}
.stats__lead b{font-weight:700}
.donut{position:absolute;left:56px;width:160px;height:160px}
.donut__label{position:absolute;left:56px;width:160px;text-align:center;font-family:'Montserrat',sans-serif;font-weight:600;font-size:13px;letter-spacing:1px;color:#fff}
.legend{position:absolute;left:250px;list-style:none;color:#dce6ef;font-size:11px}
.legend li{display:flex;align-items:center;height:21.5px}
.legend .pct{width:36px;text-align:right;font-weight:700;color:#fff;font-size:10.5px}
.legend .sw{width:11px;height:11px;border-radius:50%;margin:0 12px 0 10px}
.stats__note{position:absolute;left:58px;top:792px;font-size:8.5px;color:#c9d5e0}
.stats__folio{position:absolute;left:58px;top:818px;color:#93a5b6}
.stats__url{position:absolute;left:238px;top:813px}

/* contact */
.contact__photo{left:0;top:0;width:100%;height:170px}
.contact__thanks{position:absolute;left:58px;top:148px;font-family:'Montserrat',sans-serif;font-weight:600;font-size:19px;line-height:30px;color:#fff}
.contact__thanks span{color:var(--teal)}
.hq{position:absolute;top:285px;width:238px;text-align:center;color:#fff}
.hq h3{font-family:'Montserrat',sans-serif;font-weight:600;font-size:14px;letter-spacing:1.5px;line-height:18px;height:42px}
.hq__map{position:relative;width:238px;height:230px;background:linear-gradient(145deg,#f1f3f5,#d9dee3);margin-top:8px}
.hq__map svg{position:absolute;left:101px;top:90px}
.hq address{font-style:normal;font-size:13px;line-height:17px;margin-top:20px;color:#e8eef4}
.contact__foot{position:absolute;left:0;top:728px;width:100%;height:132px;background:var(--paper)}
.contact__foot .links{position:absolute;left:58px;top:36px;line-height:22px}
.contact__foot .brand{position:absolute;right:50px;top:48px}
</style>
</head>
<body>

<!-- Page 1 — Cover -->
<section class="page page--cover">
  <header class="cover__head">
    <div class="brand"><span class="brand__dot"></span>HARLOW &amp; ASSOCIATES</div>
  </header>
  <div class="photo cover__photo" role="img" aria-label="Scientists in cleanroom suits working with microscopes in a laboratory"></div>
  <h1 class="cover__title">RECRUITERS<br>IN LIFE SCIENCES.<br><span>FINDING THE BEST<br>TALENTS WORLDWIDE.</span></h1>
  <div class="cover__text">
    <p>We are an international recruiting boutique agency specialized in life sciences. In the last 3 decades, we have appointed thousands of professionals globally.</p>
    <p>Our firm is known for being highly committed and able to deliver great results within budget and timing constraints.</p>
  </div>
  <div class="url cover__url">www.harlowassociates.com</div>
</section>

<!-- Page 2 — Clients -->
<section class="page page--clients">
  <div class="clients__sheet">
    <div class="brand"><span class="brand__dot"></span>HARLOW &amp; ASSOCIATES</div>
    <div class="logo-grid logo-grid--top">
      <div class="logo">Varnelio</div><div class="logo">Quessa dx</div><div class="logo">Ottrel Pharma</div><div class="logo">Zimvant</div><div class="logo">Trevagen</div><div class="logo">Alquora</div>
      <div class="logo">Helmyra</div><div class="logo">Biovessa</div><div class="logo">Opraline</div><div class="logo">Kyvoro</div><div class="logo">Velmarin</div><div class="logo">Herbavique</div>
      <div class="logo">Corvessa</div><div class="logo">Atlumbe</div><div class="logo">Datrevo</div><div class="logo">Renquist</div><div class="logo">Haldrova</div><div class="logo">Volquera</div>
      <div class="logo">Kenvel Labs</div><div class="logo">Lumvessa</div><div class="logo">Bioqastra</div><div class="logo">Codrevia</div><div class="logo">Genquara</div><div class="logo">Galvessor</div>
      <div class="logo">Bovrandis</div><div class="logo">Tesselva</div><div class="logo">Enerquist</div><div class="logo">Soramiva</div><div class="logo">Oculvane</div><div class="logo">Nordquell</div>
      <div class="logo">Ypsavel</div><div class="logo">Calvinera</div><div class="logo">Radquellis</div><div class="logo">Trimvaro</div><div class="logo">Polyquessa</div><div class="logo">Diavrelle</div>
    </div>
    <div class="logo-grid logo-grid--bottom">
      <div class="logo">Phytrava</div><div class="logo">Merquello</div><div class="logo">Grenvoss Health</div><div class="logo">Ferrovane</div><div class="logo">Novquilla</div><div class="logo">Cartelvo</div>
      <div class="logo">Dermivane</div><div class="logo">Crestolva</div><div class="logo">Elmquist River</div><div class="logo">Petivale</div><div class="logo">Debravo</div><div class="logo">Vectrelle</div>
      <div class="logo">Laitavique</div><div class="logo">Signovra</div><div class="logo">Quorvelle</div><div class="logo">Galvenna</div><div class="logo">Osmiquar</div><div class="logo">NVQ Bio</div>
      <div class="logo">Berlovia</div><div class="logo">Macrevo</div><div class="logo">Isperalis</div><div class="logo">Lysquenne</div><div class="logo">Institut Varquelle</div><div class="logo">Medvoltra</div>
      <div class="logo">Toxquilab</div><div class="logo">Arvessel</div><div class="logo">Terravique Bio</div><div class="logo">GQM Health</div><div class="logo">Nestavora</div><div class="logo">Nuovaquel</div>
      <div class="logo">Garbellis</div><div class="logo">Lindquara</div><div class="logo">Novessia</div><div class="logo">Quellabs</div><div class="logo">Orvasquin</div><div class="logo">Mogravel</div>
    </div>
    <div class="clients__foot">
      <span class="folio">2 | Harlow &amp; Associates</span>
      <span class="url">www.harlowassociates.com</span>
      <span class="note">*Based on the past 5 years.</span>
    </div>
  </div>
  <div class="clients__band">
    <div class="band__small">Our clients<br>range from</div>
    <div class="band__chev">»</div>
    <div class="band__big">INNOVATIVE<br>START-UPS</div>
    <div class="band__to">to</div>
    <div class="band__big">FORTUNE 500<br>COMPANIES</div>
  </div>
</section>

<!-- Page 3 — Offices -->
<section class="page page--offices">
  <div class="rule"></div>
  <div class="offices__intro">
    <p>Harlow &amp; Associates' global success is driven by our multi-cultural team's ability to orchestrate an operational, innovative and direct approach to recruiting.</p>
    <p>Thanks to our global presence and proprietary offices in Europe and in the U.S., we have placed thousands of professionals in companies over <b>30 countries</b> and <b>5 continents</b>.</p>
  </div>
  <div class="label" style="top:228px">Offices in:</div>
  <div class="map" role="img" aria-label="World map highlighting the U.S., Brazil, Europe, North Africa, South Africa and China"></div>
  <svg class="pin-lines" width="608" height="860" aria-hidden="true">
    <g stroke="#3aa0dc" stroke-width="1" fill="none">
      <line x1="160" y1="284" x2="160" y2="400"/>
      <line x1="306" y1="284" x2="306" y2="380"/>
      <polyline points="460,284 460,300 360,300 360,370"/>
      <polyline points="236,570 236,520 190,520"/>
      <polyline points="388,570 388,520 330,520 330,400"/>
    </g>
  </svg>
  <div class="city" style="left:105px;top:258px">BOSTON</div>
  <div class="city" style="left:251px;top:258px">PARIS</div>
  <div class="city" style="left:405px;top:258px">COPENHAGEN</div>
  <div class="city" style="left:181px;top:570px">MIAMI</div>
  <div class="city" style="left:333px;top:570px">LAUSANNE</div>
  <div class="label" style="top:640px">Appointments in the last 12 months in:</div>
  <svg class="arc" width="608" height="860" aria-hidden="true">
    <path d="M0 860 Q304 640 608 860" fill="#e7ebef" stroke="#5f7488" stroke-width="1"/>
    <g stroke="#5f7488" stroke-width=".8" fill="none">
      <line x1="100" y1="745" x2="155" y2="860"/>
      <line x1="155" y1="720" x2="155" y2="860"/>
      <line x1="225" y1="700" x2="155" y2="860"/>
      <line x1="310" y1="696" x2="420" y2="860"/>
      <line x1="400" y1="715" x2="420" y2="860"/>
      <line x1="470" y1="750" x2="420" y2="860"/>
      <path d="M40 860 Q304 730 570 860"/>
    </g>
  </svg>
  <div class="bubble" style="left:73px;top:718px">U.S.</div>
  <div class="bubble" style="left:128px;top:693px">Brazil</div>
  <div class="bubble" style="left:206px;top:673px">Europe</div>
  <div class="bubble" style="left:290px;top:669px">North<br>Africa</div>
  <div class="bubble" style="left:372px;top:688px">South<br>Africa</div>
  <div class="bubble" style="left:443px;top:718px">China</div>
  <div class="url offices__url">www.harlowassociates.com</div>
  <div class="folio offices__folio">Harlow &amp; Associates | 3</div>
</section>

<!-- Page 4 — Statistics -->
<section class="page page--stats">
  <div class="stats__lead">
    <p>We cover <b>all sectors</b> and <b>all functions</b> within <b>Life Sciences</b>.</p>
    <p>Each client is <b>unique</b>.</p>
    <p style="margin-top:4px">Our solutions are <b>tailor-made</b> to your organization.</p>
  </div>

  <svg class="donut" style="top:257px" viewBox="0 0 160 160" aria-label="Sectors breakdown">
    <g fill="none" stroke-width="20" transform="rotate(-90 80 80)">
      <circle cx="80" cy="80" r="66" pathLength="100" stroke="var(--blue)" stroke-dasharray="31 69" stroke-dashoffset="0"/>
      <circle cx="80" cy="80" r="66" pathLength="100" stroke="var(--sea)" stroke-dasharray="8 92" stroke-dashoffset="-31"/>
      <circle cx="80" cy="80" r="66" pathLength="100" stroke="var(--teal)" stroke-dasharray="23 77" stroke-dashoffset="-39"/>
      <circle cx="80" cy="80" r="66" pathLength="100" stroke="var(--lime)" stroke-dasharray="9 91" stroke-dashoffset="-62"/>
      <circle cx="80" cy="80" r="66" pathLength="100" stroke="var(--purple)" stroke-dasharray="9 91" stroke-dashoffset="-71"/>
      <circle cx="80" cy="80" r="66" pathLength="100" stroke="#2f7a8a" stroke-dasharray="3 97" stroke-dashoffset="-80"/>
      <circle cx="80" cy="80" r="66" pathLength="100" stroke="var(--grey)" stroke-dasharray="3 97" stroke-dashoffset="-83"/>
      <circle cx="80" cy="80" r="66" pathLength="100" stroke="#ffffff" stroke-dasharray="14 86" stroke-dashoffset="-86"/>
    </g>
  </svg>
  <div class="donut__label" style="top:329px">SECTORS</div>
  <ul class="legend" style="top:252px">
    <li><span class="pct">31%</span><span class="sw" style="background:var(--blue)"></span>Biotech</li>
    <li><span class="pct">8%</span><span class="sw" style="background:var(--sea)"></span>Medtech</li>
    <li><span class="pct">23%</span><span class="sw" style="background:var(--teal)"></span>Medical Device</li>
    <li><span class="pct">9%</span><span class="sw" style="background:var(--lime)"></span>Digital Health</li>
    <li><span class="pct">9%</span><span class="sw" style="background:var(--purple)"></span>Nutrition</li>
    <li><span class="pct">3%</span><span class="sw" style="background:#2f7a8a"></span>Animal Health</li>
    <li><span class="pct">3%</span><span class="sw" style="background:var(--grey)"></span>Hospitals &amp; Clinics</li>
    <li><span class="pct">14%</span><span class="sw" style="background:#fff"></span>Pharma</li>
  </ul>

  <svg class="donut" style="top:428px" viewBox="0 0 160 160" aria-label="Seniority breakdown">
    <g fill="none" stroke-width="20" transform="rotate(-90 80 80)">
      <circle cx="80" cy="80" r="66" pathLength="100" stroke="var(--lime)" stroke-dasharray="9.1 90.9" stroke-dashoffset="0"/>
      <circle cx="80" cy="80" r="66" pathLength="100" stroke="var(--blue)" stroke-dasharray="33.4 66.6" stroke-dashoffset="-9.1"/>
      <circle cx="80" cy="80" r="66" pathLength="100" stroke="#ffffff" stroke-dasharray="23.6 76.4" stroke-dashoffset="-42.5"/>
      <circle cx="80" cy="80" r="66" pathLength="100" stroke="var(--teal)" stroke-dasharray="33.9 66.1" stroke-dashoffset="-66.1"/>
    </g>
  </svg>
  <div class="donut__label" style="top:500px">SENIORITY</div>
  <ul class="legend" style="top:469px">
    <li><span class="pct">9.1%</span><span class="sw" style="background:var(--lime)"></span>Board Members</li>
    <li><span class="pct">33.4%</span><span class="sw" style="background:var(--blue)"></span>Top Management</li>
    <li><span class="pct">23.6%</span><span class="sw" style="background:#fff"></span>Expert Management</li>
    <li><span class="pct">33.9%</span><span class="sw" style="background:var(--teal)"></span>Middle Management</li>
  </ul>

  <svg class="donut" style="top:600px" viewBox="0 0 160 160" aria-label="Function breakdown">
    <g fill="none" stroke-width="20" transform="rotate(-90 80 80)">
      <circle cx="80" cy="80" r="66" pathLength="100" stroke="var(--lime)" stroke-dasharray="6.8 93.2" stroke-dashoffset="0"/>
      <circle cx="80" cy="80" r="66" pathLength="100" stroke="var(--sea)" stroke-dasharray="4.2 95.8" stroke-dashoffset="-6.8"/>
      <circle cx="80" cy="80" r="66" pathLength="100" stroke="var(--teal)" stroke-dasharray="27.5 72.5" stroke-dashoffset="-11"/>
      <circle cx="80" cy="80" r="66" pathLength="100" stroke="#ffffff" stroke-dasharray="29 71" stroke-dashoffset="-38.5"/>
      <circle cx="80" cy="80" r="66" pathLength="100" stroke="var(--grey)" stroke-dasharray="4.2 95.8" stroke-dashoffset="-67.5"/>
      <circle cx="80" cy="80" r="66" pathLength="100" stroke="var(--purple)" stroke-dasharray="9.2 90.8" stroke-dashoffset="-71.7"/>
      <circle cx="80" cy="80" r="66" pathLength="100" stroke="var(--blue)" stroke-dasharray="19.1 80.9" stroke-dashoffset="-80.9"/>
    </g>
  </svg>
  <div class="donut__label" style="top:672px">FUNCTION</div>
  <ul class="legend" style="top:608px">
    <li><span class="pct">6.8%</span><span class="sw" style="background:var(--lime)"></span>Quality</li>
    <li><span class="pct">4.2%</span><span class="sw" style="background:var(--sea)"></span>Finance/Legal</li>
    <li><span class="pct">27.5%</span><span class="sw" style="background:var(--teal)"></span>Medical &amp; Regulatory Affairs/Market Access</li>
    <li><span class="pct">29%</span><span class="sw" style="background:#fff"></span>Sales/Business Development</li>
    <li><span class="pct">4.2%</span><span class="sw" style="background:var(--grey)"></span>HR</li>
    <li><span class="pct">9.2%</span><span class="sw" style="background:var(--purple)"></span>Industrial</li>
    <li><span class="pct">19.1%</span><span class="sw" style="background:var(--blue)"></span>R&amp;D</li>
  </ul>

  <div class="stats__note">*Based on the last 5 years results.</div>
  <div class="folio stats__folio">4 | Harlow &amp; Associates</div>
  <div class="url stats__url">www.harlowassociates.com</div>
</section>

<!-- Page 5 — Contact -->
<section class="page page--contact">
  <div class="photo contact__photo" role="img" aria-label="Laboratory bench with glassware and a researcher at work"></div>
  <div class="contact__thanks">Thank you for your consideration.<br><span>We are looking forward to speaking with you.</span></div>

  <div class="hq" style="left:55px">
    <h3>NORTH AMERICA<br>HEADQUARTERS</h3>
    <div class="hq__map" role="img" aria-label="Street map of the Boston office area">
      <svg width="36" height="40" viewBox="0 0 24 28" aria-hidden="true"><path d="M12 1C6.5 1 3 5 3 10c0 6.5 9 16 9 16s9-9.5 9-16c0-5-3.5-9-9-9z" fill="var(--blue)"/><circle cx="12" cy="10" r="3.5" fill="#fff"/></svg>
    </div>
    <address>18 Harbor Lane<br>Boston, MA, 02110<br>United States of America</address>
  </div>
  <div class="hq" style="left:315px">
    <h3>EMEA<br>HEADQUARTERS</h3>
    <div class="hq__map" role="img" aria-label="Street map of the Paris office area">
      <svg width="36" height="40" viewBox="0 0 24 28" aria-hidden="true"><path d="M12 1C6.5 1 3 5 3 10c0 6.5 9 16 9 16s9-9.5 9-16c0-5-3.5-9-9-9z" fill="var(--blue)"/><circle cx="12" cy="10" r="3.5" fill="#fff"/></svg>
    </div>
    <address>42 Rue Valmont<br>75008 Paris, France</address>
  </div>

  <footer class="contact__foot">
    <div class="links url">talent@harlowassociates.com<br>www.harlowassociates.com</div>
    <div class="brand"><span class="brand__dot"></span>HARLOW &amp; ASSOCIATES</div>
  </footer>
</section>

</body>
</html>
```